Actors Postcard Design

I need a postcard designed for me. I am an actor, voice over artist and technical adviser for tv, film and videogames. I am open to color ideas. My photos are in black and white so something to make those stand out a bit. Masculine colors like dark blue etc..I have seen some of your designs with 3 photos which I liked. Perhaps a 2-3 photo scheme. Back of postcard to contain my resume. Want it to look professional and not cartoonish (since I mentioned video games). Front to have photos and job title and contact info

Please take my color direction lightly, I am open to all color schemes. light or dark. You are the professionals. Am looking forward to seeing what all of you come up with. Thanks

Tv

```html
<!DOCTYPE html>
<html lang="en">
<head>
<meta charset="utf-8">
<title>Daniel Korwin – Actor Postcard</title>
<link rel="stylesheet" href="https://fonts.googleapis.com/css2?family=Montserrat:wght@300;400;500;600;700&display=swap">
<style>
  :root {
    --accent: #1b7fd8;
    --ink: #4a4a4a;
    --muted: #8a8a8a;
    --rule: #c8c8c8;
    --paper: #ffffff;
    --backdrop: #ffffff;
    --photo-dark: #3a3a3a;
    --photo-mid: #8c8c8c;
    --photo-light: #c9c9c9;
  }
  * { box-sizing: border-box; margin: 0; padding: 0; }
  html, body {
    width: 810px; height: 1200px; overflow: hidden;
    background: var(--backdrop);
    font-family: "Montserrat", Arial, sans-serif;
    color: var(--ink);
  }
  .canvas { position: relative; width: 810px; height: 1200px; }

  .card {
    position: absolute; left: 29px; width: 744px;
    background: var(--paper);
    box-shadow: 0 2px 8px rgba(0,0,0,0.22);
  }
  .card--front { top: 13px; height: 569px; }
  .card--back { top: 613px; height: 577px; }

  /* Front */
  .hero {
    position: absolute; left: 19px; top: 20px; width: 707px; height: 529px;
    background:
      radial-gradient(ellipse 35% 48% at 72% 42%, var(--photo-light) 0%, rgba(200,200,200,0) 70%),
      linear-gradient(100deg, #9a9a9a 0%, #7c7c7c 45%, var(--photo-dark) 100%);
  }
  .hero__name {
    position: absolute; left: 60px; top: 258px;
    font-size: 24px; line-height: 1.2; letter-spacing: 0.5px;
  }
  .hero__name .first { display: block; color: var(--accent); font-weight: 700; }
  .hero__name .last { display: block; color: #fff; font-weight: 300; }
  .hero__roles {
    position: absolute; left: 0; right: 0; bottom: 36px;
    text-align: center; color: #fff;
    font-size: 13px; font-weight: 500; letter-spacing: 4.4px;
  }
  .hero__roles .sep { margin: 0 12px; letter-spacing: 0; }

  /* Back */
  .shot { position: absolute; top: 57px; height: 173px; }
  .shot--action {
    left: 0; width: 244px;
    background: linear-gradient(90deg, #bdbdbd 0%, #6a6a6a 55%, #2e2e2e 80%, #b0b0b0 100%);
  }
  .shot--studio {
    left: 252px; width: 248px;
    background: linear-gradient(90deg, #5e5e5e 0%, #2a2a2a 30%, #9a9a9a 65%, #d6d6d6 100%);
  }
  .back__name {
    position: absolute; left: 559px; top: 120px;
    font-size: 18px; line-height: 1.2; letter-spacing: 0.4px;
  }
  .back__name .first { display: block; color: var(--accent); font-weight: 700; }
  .back__name .last { display: block; color: var(--muted); font-weight: 400; }

  .stats {
    position: absolute; left: 37px; top: 281px; right: 20px;
    display: flex; align-items: center;
    font-size: 11.5px; color: var(--ink);
  }
  .stats b { color: var(--accent); font-weight: 600; }
  .stats .stat { margin-right: 16px; }
  .stats .divider { width: 1px; height: 15px; background: var(--rule); margin: 0 16px 0 8px; }
  .stats .contact { color: var(--accent); font-weight: 600; margin-right: 14px; }

  .column { position: absolute; top: 326px; }
  .column--training { left: 37px; width: 320px; }
  .column--advising { left: 396px; width: 310px; top: 318px; }
  .column-rule {
    position: absolute; left: 353px; top: 328px; width: 1px; height: 218px;
    background: var(--rule);
  }
  .section-title {
    color: var(--accent); font-size: 20px; font-weight: 500; line-height: 1.2;
  }
  .lede { font-size: 12.5px; line-height: 1.3; }
  .group { margin-top: 22px; }
  .column--advising .group { margin-top: 14px; }
  .group__title { color: var(--accent); font-size: 12.5px; font-weight: 700; line-height: 1.35; }
  .group p, .group li { font-size: 12.5px; line-height: 1.35; list-style: none; }
  .group .note { font-style: italic; font-size: 11px; line-height: 1.3; }
</style>
</head>
<body>
<main class="canvas">

  <section class="card card--front" aria-label="Postcard front">
    <div class="hero" role="img" aria-label="Black and white head-and-shoulders portrait of the actor outdoors, soft blurred greenery behind">
      <h1 class="hero__name"><span class="first">DANIEL</span><span class="last">KORWIN</span></h1>
      <p class="hero__roles">ACTOR<span class="sep">|</span>VOICE OVER ARTIST<span class="sep">|</span>TECHNICAL ADVISOR</p>
    </div>
  </section>

  <section class="card card--back" aria-label="Postcard back – resume">
    <div class="shot shot--action" role="img" aria-label="Black and white photo of the actor aiming a tactical rifle"></div>
    <div class="shot shot--studio" role="img" aria-label="Black and white photo of the actor smiling beside a studio microphone"></div>
    <h2 class="back__name"><span class="first">DANIEL</span><span class="last">KORWIN</span></h2>

    <div class="stats">
      <span class="stat"><b>Height:</b> 6'0"</span>
      <span class="stat"><b>Weight:</b> 180</span>
      <span class="stat"><b>Hair:</b> Blond</span>
      <span class="stat"><b>Eyes:</b> Green</span>
      <span class="divider"></span>
      <span class="contact">danielkorwin@mailbox.net</span>
      <span>555-014-2276</span>
    </div>

    <div class="column column--training">
      <h3 class="section-title">Training/Experience</h3>
      <div class="group">
        <h4 class="group__title">Acting</h4>
        <ul>
          <li>Marlow Acting School - 1.5 yrs</li>
          <li>Stagefront Studio International – On Camera 2yrs</li>
          <li>Highland Acting Coach – 5 day intensive</li>
        </ul>
      </div>
      <div class="group">
        <h4 class="group__title">Voice Over</h4>
        <p>Voice Lab – Daybreak Conservatory (commercial, narration, etc…)</p>
        <p class="note">- Adv Daybreak Conservatory</p>
        <p class="note">- 4 day Character Intensive</p>
      </div>
    </div>

    <div class="column-rule"></div>

    <div class="column column--advising">
      <h3 class="section-title">Technical Advising</h3>
      <p class="lede">DEA Special Agent – 10.5 yrs</p>
      <div class="group">
        <p><span class="group__title">Extensive Firearms Training</span> – DEA, Northline Tactics, Former Delta Members, Army ODA. Defensive Tactics, Breaching, Vehicle Containment, Surveillance, etc…</p>
      </div>
      <div class="group">
        <h4 class="group__title">Special Skills</h4>
        <p>15 yrs martial arts (Gung Fu, Judo, Tai Chi, Kenjutsu), EMT, Personal Trainer, Scuba, Snowboarding, Snowshoeing, Alpine Mountaineering, Archery, Mountainbiking, SUP, Blacksmithing, Carpentry 7yrs. Fluent Polish.</p>
      </div>
    </div>
  </section>

</main>
</body>
</html>
```